Local Chiropractor Needs Up Scale Webdesign

This website needs to have an upscale look with a very modern feel. Below is the information and websites to reference

Add Logo that is attached

Build a color scheme similar to this website image titled "chiro-1"

Must Include these pages in a horizontal menu bar in this order:
Home, Meet Our Staff, Patient Testimonials, Videos, Work Place Wellness, Contact

Build a "classy looking" Make An Appointment Button into the header with the contact info below

Phone Number:
555-314-2760

Address:
4182 Maple Fern Court, #305
Willowmere, LK 55492

This website needs 4 rotating banners. Please reference a layout similar to this for the banners: http://drkelrom.com/. However design it nicer than this website, this website is very boring and doesn't flow with the colors properly

Below are the description for each banner

Rotating Banner #1
Use Image: Pediatrics
Two lines of text. First line title line, second description. Use Latin text for fill

Rotating Banner #2
Use Image: Aging Gracefully

Rotating Banner #3
Use Image: Pregnancy

Rotating Banner #4
Use Image: Athletics

I'd like to see a free consultation box similar to the "chiro-1" image. Fields to include are: First Name, Last Name, Phone Number, Comments.

For the body, please fill it with latin text. Please design a professional body layout. You can include a box in the right column for the hours

Office Hours
Monday: 8:00-11:00, 2:00-5:00
Tuesday: 8:30-11:00, 2:00-5:30
Wednesday: 8:00-11:00, 2:00-5:00
Thursday: 10:00-12:00, 2:30-5:00
Friday: 8:00-10:00, 1:00-5:00
Saturday: Closed
Sunday: Closed

For the footer please design something similar to the: http://drkelrom.com/

Also include in the Footer: Powered by Brightpath Site Co

Chiropractor

```html
<!DOCTYPE html>
<html lang="en">
<head>
<meta charset="utf-8">
<title>Evergreen Path Chiropractic</title>
<link href="https://fonts.googleapis.com/css2?family=Open+Sans:wght@400;600;700&family=Roboto+Slab:wght@400;700&display=swap" rel="stylesheet">
<style>
:root{
  --green:#8cbf1f;
  --green-dark:#6e9a12;
  --orange:#d98a1c;
  --ink:#333;
  --muted:#666;
  --line:#dcdcdc;
  --dark:#2b2b2b;
  --darker:#1d1d1d;
  --blue:#1ab3e8;
  --red:#d8201e;
  --panel:#f2f2f2;
}
*{box-sizing:border-box;margin:0;padding:0}
html,body{width:1200px;height:2343px;overflow:hidden}
body{position:relative;background:#fff;font-family:"Open Sans",Arial,sans-serif;color:var(--ink);font-size:14px}
.abs{position:absolute}
.slab{font-family:"Roboto Slab",Georgia,serif}

/* header */
.topline{left:0;top:0;width:1200px;height:5px;background:var(--orange)}
.header{left:0;top:5px;width:1200px;height:117px;background:linear-gradient(#fff,#f1f1f1)}
.brand{display:flex;align-items:center;gap:14px}
.brand-dot{width:56px;height:56px;border-radius:50%;background:var(--green)}
.brand-name{font-size:30px;font-weight:600;color:var(--green);line-height:1.1}
.appt{left:633px;width:221px;height:60px;border-radius:6px;background:linear-gradient(#4a4a4a,#1f1f1f);display:flex;align-items:center;gap:14px;padding-left:16px;color:#fff;box-shadow:0 2px 3px rgba(0,0,0,.3)}
.appt small{display:block;font-size:12px;color:#ccc}
.appt b{font-size:16px;letter-spacing:.5px}
.contact-top{left:893px;font-size:13px;color:var(--ink);line-height:20px}
.contact-top div{display:flex;gap:10px;margin-bottom:8px}

/* nav */
.nav{left:0;top:122px;width:1200px;height:48px;background:linear-gradient(#9ccc2e,var(--green));display:flex;padding-left:100px}
.nav a{color:#fff;text-decoration:none;font-size:16px;padding:0 14px;line-height:48px}
.nav a.active{background:#fff;color:var(--ink);margin-top:4px;line-height:44px}

/* hero */
.hero{left:0;top:170px;width:1200px;height:502px;background:linear-gradient(120deg,#5b6b34 0%,#a2a05c 35%,#c9c39a 55%,#4f5e2c 100%)}
.hero-title{right:132px;top:290px;font-size:46px;font-weight:700;color:#fff;text-shadow:0 2px 4px rgba(0,0,0,.5)}
.hero-text{right:132px;top:380px;width:380px;text-align:right;font-size:15px;color:#fff;font-weight:600;text-shadow:0 1px 3px rgba(0,0,0,.6);line-height:20px}
.hero-btn{left:906px;top:470px;width:157px;height:46px;background:var(--green);color:#fff;font-size:16px;display:flex;align-items:center;justify-content:center}
.arrow{width:50px;height:50px;border-radius:50%;background:rgba(255,255,255,.5);display:flex;align-items:center;justify-content:center}

/* consultation */
.consult{left:763px;top:594px;width:338px;height:609px;background:var(--panel);box-shadow:0 0 4px rgba(0,0,0,.2)}
.consult-head{height:88px;background:linear-gradient(#3d3d3d,#1e1e1e);display:flex;align-items:center;gap:20px;padding-left:22px;color:#fff}
.consult-head small{display:block;font-size:13px;color:#bbb}
.consult-head b{font-size:19px;display:block}
.consult-head em{font-style:normal;color:var(--green);font-size:21px;font-weight:700}
.consult-body{padding:16px 22px}
.consult-body h3{font-size:18px;font-weight:400;margin-bottom:20px;color:var(--ink)}
.field label{display:block;font-size:13px;margin-bottom:6px}
.field .box{height:44px;background:#fff;border:1px solid #bbb;margin-bottom:18px;width:300px}
.field .box.tall{height:112px}
.submit{width:106px;height:40px;background:var(--green);color:#fff;display:flex;align-items:center;justify-content:center;font-size:14px}

/* main */
.sec-title{font-size:40px;color:var(--ink);display:flex;align-items:baseline;gap:12px}
.sec-title em{font-family:"Open Sans",sans-serif;font-style:italic;font-size:13px;color:var(--orange)}
.body-text{font-size:14px;line-height:23px;color:var(--muted)}
.photo{background:linear-gradient(160deg,#d9dde0,#a9b3bb)}
.btn-grey{width:120px;height:34px;background:linear-gradient(#e6e6e6,#cfcfcf);color:var(--ink);font-size:14px;display:flex;align-items:center;justify-content:center}
.divider{left:100px;width:642px;height:1px;background:var(--line)}
.staff{top:1255px;width:192px}
.staff .photo{height:197px;background:linear-gradient(#f3f3f3,#cfd6dc)}
.staff h4{font-size:15px;margin-top:24px}
.staff p{font-size:12px;color:var(--muted);margin-top:4px}
.staff .btn-grey{margin-top:22px;width:126px}
.circ{width:38px;height:38px;border-radius:50%;background:#ddd;display:flex;align-items:center;justify-content:center}

/* sidebar */
.testi{left:763px;top:1255px;width:338px;height:99px;background:linear-gradient(#27c0f3,var(--blue));display:flex;align-items:center;gap:22px;padding-left:22px;color:#fff}
.side-head small{display:block;font-size:13px}
.side-head b{font-size:19px;display:block;line-height:23px}
.hours-head{left:763px;top:1369px;width:338px;height:102px;background:linear-gradient(#9fd02f,var(--green));display:flex;align-items:center;gap:22px;padding-left:22px;color:#fff}
.hours{left:763px;top:1471px;width:338px;height:481px;background:#f5f5f5;padding:6px 22px 0;box-shadow:0 0 4px rgba(0,0,0,.15)}
.hours-row{display:flex;border-bottom:1px solid var(--line);font-size:14px;padding:9px 0;line-height:22px}
.hours-row .d{width:168px;font-weight:700}
.hours-row.h{font-style:italic;color:var(--muted);font-weight:400}
.hours-row.h .d{font-weight:400}
.closed{color:var(--red);font-weight:700}

/* footer */
.footer{left:0;top:1989px;width:1200px;height:312px;background:var(--dark);color:#ddd}
.footer h3{font-size:20px;font-weight:400;color:#fff}
.f-item{display:flex;gap:14px;font-size:14px;line-height:22px}
.f-item a{color:#fff;font-weight:700;text-decoration:underline}
.map{left:341px;top:86px;width:377px;height:156px;background:linear-gradient(135deg,#e9e6df,#cfd6cf);border:4px solid #fff}
.ftable{left:763px;top:76px;width:338px;font-size:13px}
.ftable div{display:flex;padding:6px 0;border-bottom:1px solid #444}
.ftable span:first-child{width:170px}
.ftable span:nth-child(2){width:100px}
.bottom{left:0;top:2301px;width:1200px;height:42px;background:var(--darker);color:#999;font-size:11px;display:flex;align-items:center;padding:0 100px;justify-content:space-between}
.bottom nav{display:flex;gap:24px;align-items:center}
.bottom nav a{color:#ddd;text-decoration:underline}
</style>
</head>
<body>
<div class="abs topline"></div>
<header class="abs header">
  <div class="abs brand" style="left:100px;top:17px"><span class="brand-dot"></span><span class="brand-name">Evergreen Path<br><span style="font-size:18px">Chiropractic</span></span></div>
  <div class="abs appt" style="top:31px">
    <svg width="30" height="30" viewBox="0 0 30 30"><rect x="2" y="5" width="26" height="23" rx="3" fill="#e53b2c"/><rect x="5" y="12" width="20" height="13" fill="#fff"/><rect x="8" y="2" width="3" height="7" fill="#ccc"/><rect x="19" y="2" width="3" height="7" fill="#ccc"/></svg>
    <div><small>make an</small><b>APPOINTMENT</b></div>
  </div>
  <div class="abs contact-top" style="top:19px">
    <div><svg width="14" height="16" viewBox="0 0 14 16"><path d="M3 1l3 4-2 2c1 2 3 4 5 5l2-2 3 3-2 2C6 15 0 9 1 3z" fill="#8cbf1f"/></svg>555-314-2760</div>
    <div><svg width="14" height="18" viewBox="0 0 14 18"><path d="M7 0a7 7 0 0 0-7 7c0 5 7 11 7 11s7-6 7-11a7 7 0 0 0-7-7z" fill="#8cbf1f"/><circle cx="7" cy="7" r="2.5" fill="#fff"/></svg><span>4182 Maple Fern Court, #305<br>Willowmere, LK 55492</span></div>
  </div>
</header>
<nav class="abs nav">
  <a class="active">Home</a><a>Meet Our Staff</a><a>Patient Testimonial</a><a>Videos</a><a>Workplace Wellness</a><a>Contact Us</a>
</nav>

<section class="abs hero" role="img" aria-label="Two smiling older women jogging along a wooded park path"></section>
<h1 class="abs hero-title slab">Aging Gracefully</h1>
<p class="abs hero-text">Nullam id nibh et ligula ultrices consequat quis venenatis elit. Mauris a magna dignissim, aliquam risus elementum, mattis.</p>
<div class="abs hero-btn">Read More</div>
<div class="abs arrow" style="left:48px;top:392px"><svg width="14" height="20"><path d="M11 2L3 10l8 8" stroke="#fff" stroke-width="3" fill="none"/></svg></div>
<div class="abs arrow" style="left:1100px;top:392px"><svg width="14" height="20"><path d="M3 2l8 8-8 8" stroke="#fff" stroke-width="3" fill="none"/></svg></div>

<aside class="abs consult">
  <div class="consult-head">
    <svg width="56" height="40" viewBox="0 0 56 40"><rect width="56" height="40" rx="3" fill="#f4a21c"/><path d="M2 3l26 20L54 3" stroke="#fff" stroke-width="3" fill="none"/></svg>
    <div><small>contact us now to get</small><b>FREE CONSULTATION</b><em>TODAY</em></div>
  </div>
  <form class="consult-body">
    <h3 class="slab">Wellness Begins Here</h3>
    <div class="field"><label>First Name *</label><div class="box"></div></div>
    <div class="field"><label>Last Name *</label><div class="box"></div></div>
    <div class="field"><label>Phone No *</label><div class="box"></div></div>
    <div class="field"><label>Comments *</label><div class="box tall"></div></div>
    <div class="submit">Submit</div>
  </form>
</aside>

<h2 class="abs sec-title slab" style="left:100px;top:700px">About Us <em>Who we are &amp; what we do</em></h2>
<p class="abs body-text" style="left:100px;top:772px;width:392px">Nullam id nibh et ligula ultrices consequat quis venenatis elit. Mauris a magna dignissim, aliquam risus elementum, mattis odio. Fusce semper dolor metus, eget vehicula risus interdum consectetur. Praesent tincidunt urna malesuada, laoreet mi cursus, ornare ante.<br><br>Nam fringilla risus non nisl tincidunt rhoncus. Mauris molestie posuere diam consequat imperdiet. Nullam hendrerit ultrices eros, at eleifend justo interdum nec. Sed sed tincidunt ipsum. Nullam iaculis ligula nec arcu dapibus, at condimentum lorem aliquet. Quisque mi risus, vel.</p>
<div class="abs photo" style="left:521px;top:781px;width:221px;height:307px" role="img" aria-label="Chiropractor explaining a spine model to a patient"></div>
<div class="abs btn-grey" style="left:100px;top:1086px">Read More</div>
<div class="abs divider" style="top:1161px"></div>

<h2 class="abs sec-title slab" style="left:100px;top:1188px;font-size:34px">Meet Our Staff <em>Best in the business</em></h2>
<div class="abs circ" style="left:651px;top:1196px"><svg width="10" height="14"><path d="M8 2L3 7l5 5" stroke="#fff" stroke-width="2.5" fill="none"/></svg></div>
<div class="abs circ" style="left:701px;top:1196px"><svg width="10" height="14"><path d="M2 2l5 5-5 5" stroke="#fff" stroke-width="2.5" fill="none"/></svg></div>
<div class="abs staff" style="left:100px"><div class="photo" role="img" aria-label="Portrait of a senior male doctor in a white coat"></div><h4>Dr. Harlan Pryce</h4><p>M.D Chiropractic</p><div class="btn-grey">View Doctor</div></div>
<div class="abs staff" style="left:325px"><div class="photo" role="img" aria-label="Portrait of a female doctor in a white coat"></div><h4>Dr. Mirela Voss</h4><p>M.D Chiropractic</p><div class="btn-grey">View Doctor</div></div>
<div class="abs staff" style="left:547px"><div class="photo" role="img" aria-label="Portrait of a male doctor holding a clipboard"></div><h4>Dr. Dario Fenn</h4><p>M.D Chiropractic</p><div class="btn-grey">View Doctor</div></div>
<div class="abs divider" style="top:1596px"></div>

<h2 class="abs sec-title slab" style="left:100px;top:1628px;font-size:32px">Workplace Wellbeing <em>Sound body while working</em></h2>
<div class="abs photo" style="left:100px;top:1697px;width:218px;height:172px;background:linear-gradient(160deg,#cfd3d8,#5c6670)" role="img" aria-label="Office workers meditating together at their workplace"></div>
<p class="abs body-text" style="left:362px;top:1690px;width:380px">Nullam id nibh et ligula ultrices consequat quis venenatis elit. Mauris a magna dignissim, aliquam risus elementum, mattis odio. Fusce semper dolor metus.<br><br>eget vehicula risus interdum consectetur. Praesent tincidunt urna malesuada, laoreet mi cursus, ornare ante...</p>
<div class="abs btn-grey" style="left:362px;top:1862px">Read More</div>

<div class="abs testi">
  <svg width="50" height="44" viewBox="0 0 50 44"><path d="M0 44V24C0 10 8 2 20 0v8c-6 2-9 7-9 14h9v22zM28 44V24C28 10 36 2 48 0v8c-6 2-9 7-9 14h9v22z" fill="#fff"/></svg>
  <div class="side-head"><small>see what our patients say</small><b>PATIENT<br>TESTIMONIALS</b></div>
</div>
<div class="abs hours-head">
  <svg width="54" height="54" viewBox="0 0 54 54"><circle cx="27" cy="29" r="23" fill="#fff" stroke="#e5452e" stroke-width="5"/><path d="M27 15v14l9 6" stroke="#333" stroke-width="3" fill="none"/></svg>
  <div class="side-head"><small>check out our</small><b>OFFICE HOURS</b></div>
</div>
<div class="abs hours">
  <div class="hours-row h"><span class="d">Day</span><span>Hours</span></div>
  <div class="hours-row"><span class="d">Monday</span><span>8:00-11:00<br>2:00-5:00</span></div>
  <div class="hours-row"><span class="d">Tuesday:</span><span>8:30-11:00<br>2:00-5:30</span></div>
  <div class="hours-row"><span class="d">Wednesday :</span><span>8:00-11:00<br>2:00-5:00</span></div>
  <div class="hours-row"><span class="d">Thursday:</span><span>10:00-12:00<br>2:30-5:00</span></div>
  <div class="hours-row"><span class="d">Friday:</span><span>8:00-10:00<br>1:00-5:00</span></div>
  <div class="hours-row"><span class="d">Saturday:</span><span class="closed">Closed</span></div>
  <div class="hours-row" style="border:0"><span class="d">Sunday:</span><span class="closed">Closed</span></div>
</div>

<footer class="abs footer">
  <h3 class="abs" style="left:100px;top:24px">Contact Information</h3>
  <div class="abs f-item" style="left:100px;top:82px"><svg width="14" height="16" viewBox="0 0 14 16"><path d="M3 1l3 4-2 2c1 2 3 4 5 5l2-2 3 3-2 2C6 15 0 9 1 3z" fill="#ccc"/></svg>555-314-2760</div>
  <div class="abs f-item" style="left:100px;top:124px"><svg width="14" height="18" viewBox="0 0 14 18"><path d="M7 0a7 7 0 0 0-7 7c0 5 7 11 7 11s7-6 7-11a7 7 0 0 0-7-7z" fill="#ccc"/></svg><span>4182 Maple Fern Court, #305<br>Willowmere, LK 55492<br><a>Get Directions</a></span></div>
  <div class="abs f-item" style="left:100px;top:210px"><svg width="16" height="12" viewBox="0 0 16 12"><rect width="16" height="12" fill="#ccc"/><path d="M1 1l7 6 7-6" stroke="#2b2b2b" fill="none"/></svg><a>Email Us</a></div>
  <div class="abs map" role="img" aria-label="Street map showing the clinic location with a red pin"></div>
  <h3 class="abs" style="left:763px;top:24px">Office Timings</h3>
  <div class="abs ftable">
    <div><span>Monday</span><span>8:00-11:00</span><span>2:00-5:00</span></div>
    <div><span>Tuesday:</span><span>8:30-11:00</span><span>2:00-5:30</span></div>
    <div><span>Wednesday :</span><span>8:00-11:00</span><span>2:00-5:00</span></div>
    <div><span>Thursday:</span><span>10:00-12:00</span><span>2:30-5:00</span></div>
    <div><span>Friday:</span><span>8:00-10:00</span><span>1:00-5:00</span></div>
    <div><span>Saturday:</span><span>Closed</span><span>Closed</span></div>
    <div style="border:0"><span>Sunday:</span><span>Closed</span><span>Closed</span></div>
  </div>
</footer>
<div class="abs bottom">
  <span>Copyright 2013 Evergreen Path Chiropractic. All rights reserved. Powered by Brightpath Site Co</span>
  <nav><a>Terms Of Use</a><a>Privacy Policy</a><svg width="16" height="10"><path d="M2 8l6-6 6 6" stroke="#ddd" stroke-width="2" fill="none"/></svg></nav>
</div>
</body>
</html>
```